Bright Ember Publicity is a new boutique Press Office with a small roster of well-chosen clients across an array of disciplines; from Art and Technology to Restaurants and Fashion. Based in Greenpoint Brooklyn, Bright Ember Publicity achieves outstanding results through hard work, tenacity, efficiency and a sense of humor. We need a simple, versatile and classic design. We would like each side of the card to be white text on a black background.

Boutique

```html
<!DOCTYPE html>
<html lang="en">
<head>
<meta charset="utf-8">
<title>Bright Ember Publicity — Business Card</title>
<link href="https://fonts.googleapis.com/css2?family=Libre+Baskerville:wght@400;700&display=swap" rel="stylesheet">
<style>
  :root {
    --backdrop: #3e3e3f;
    --card: #262526;
    --ink: #ffffff;
    --ink-soft: #e6e6e6;
  }
  * { margin: 0; padding: 0; box-sizing: border-box; }
  html, body {
    width: 1200px;
    height: 810px;
    overflow: hidden;
    background: var(--backdrop);
    font-family: "Libre Baskerville", "Times New Roman", serif;
    color: var(--ink);
  }
  .canvas {
    position: relative;
    width: 1200px;
    height: 810px;
    display: flex;
    align-items: center;
    justify-content: center;
    gap: 60px;
  }
  .card {
    position: relative;
    width: 510px;
    height: 320px;
    background: var(--card);
    border-radius: 22px;
  }
  .brand {
    position: absolute;
    left: 0;
    right: 0;
    text-align: center;
  }
  .brand-mark {
    display: inline-block;
    width: 14px;
    height: 14px;
    border-radius: 50%;
    background: var(--ink);
    margin-bottom: 14px;
  }
  .brand-name {
    font-size: 21px;
    font-weight: 400;
    letter-spacing: 0.18em;
    text-transform: uppercase;
    white-space: nowrap;
  }
  .card-front .brand { top: 92px; }
  .card-front .web {
    position: absolute;
    left: 0; right: 0;
    top: 200px;
    text-align: center;
    font-size: 13px;
    letter-spacing: 0.22em;
    color: var(--ink-soft);
  }
  .card-back .brand { top: 48px; }
  .contact {
    position: absolute;
    left: 52px;
    bottom: 38px;
  }
  .person-name {
    font-size: 20px;
    font-weight: 700;
    margin-bottom: 6px;
  }
  .person-role {
    font-size: 13px;
    color: var(--ink-soft);
    margin-left: 22px;
    margin-bottom: 16px;
  }
  .contact-list {
    list-style: none;
    margin-left: 42px;
  }
  .contact-list li {
    display: flex;
    align-items: center;
    gap: 9px;
    font-size: 13px;
    line-height: 22px;
    color: var(--ink-soft);
  }
  .contact-list svg { width: 12px; height: 12px; fill: var(--ink); flex: none; }
</style>
</head>
<body>
<main class="canvas">

  <section class="card card-front" aria-label="Card front">
    <div class="brand">
      <span class="brand-mark"></span>
      <p class="brand-name">Bright Ember Publicity</p>
    </div>
    <p class="web">www.brightemberpr.com</p>
  </section>

  <section class="card card-back" aria-label="Card back">
    <div class="brand">
      <span class="brand-mark"></span>
      <p class="brand-name">Bright Ember Publicity</p>
    </div>
    <div class="contact">
      <p class="person-name">Daniel Whitcombe</p>
      <p class="person-role">Owner &amp; Founder</p>
      <ul class="contact-list">
        <li>
          <svg viewBox="0 0 24 24" aria-hidden="true"><path d="M6.6 10.8a15.1 15.1 0 0 0 6.6 6.6l2.2-2.2a1 1 0 0 1 1-.25 11.4 11.4 0 0 0 3.6.57 1 1 0 0 1 1 1V20a1 1 0 0 1-1 1A17 17 0 0 1 3 4a1 1 0 0 1 1-1h3.5a1 1 0 0 1 1 1c0 1.25.2 2.45.57 3.57a1 1 0 0 1-.25 1z"/></svg>
          <span>917-555-0142</span>
        </li>
        <li>
          <svg viewBox="0 0 24 24" aria-hidden="true"><path d="M2 5h20v14H2z M3.5 6.5 12 13l8.5-6.5" fill="none" stroke="#fff" stroke-width="2"/></svg>
          <span>daniel@brightemberpr.com</span>
        </li>
        <li>
          <svg viewBox="0 0 24 24" aria-hidden="true"><circle cx="12" cy="12" r="9" fill="none" stroke="#fff" stroke-width="2"/><path d="M3 12h18M12 3c3 3 3 15 0 18M12 3c-3 3-3 15 0 18" fill="none" stroke="#fff" stroke-width="1.6"/></svg>
          <span>www.brightemberpr.com</span>
        </li>
      </ul>
    </div>
  </section>

</main>
</body>
</html>
```